Real Estate Buisiness Card

On front of card:
I would like Initials DH with scroll or circle sophisticated fonts. Dena Hartwell, Realtor/Broker, CRS/EPro, BRE # 00573846
Direct: 661-548-2907
Email: dena@bluevane4homes.example
Website:Bluevanerealestate.example
Turning Real Estate Dreams Into Realty!
Headshot

On back of card:
Team Hartwell is the Real Estate Team with Integrity & Expertise!
Certified Residential Specialist
Marketing Expert
Internet Expert
Finance Expert
Team Hartwell specializes in Residential Sales,
Distressed Properties
Investment Properties
Property Management

Blue Vane Realty logo
41720 Calloway Lane, Suite #308, Santa Clarita, CA 91350

```html
<!DOCTYPE html>
<html lang="en">
<head>
<meta charset="utf-8">
<title>Dena Hartwell – Realtor/Broker</title>
<link rel="stylesheet" href="https://fonts.googleapis.com/css2?family=Cinzel:wght@400;600;700&family=Roboto:wght@400&display=swap">
<style>
  :root {
    --bg-light: #ecebe9;
    --bg-mid: #dddcd9;
    --navy: #0f1a3c;
    --navy-deep: #0a1230;
    --ink: #1a1a1a;
    --text-blue: #16264d;
    --gold: #c99a2e;
    --gold-light: #f1d27a;
    --gold-dark: #9c7420;
  }
  * { margin: 0; padding: 0; box-sizing: border-box; }
  html, body { width: 1200px; height: 702px; overflow: hidden; background: var(--bg-light); }
  .card {
    position: relative;
    width: 1200px;
    height: 702px;
    overflow: hidden;
    background: radial-gradient(ellipse at 60% 40%, var(--bg-light) 0%, var(--bg-mid) 100%);
  }
  .headshot {
    position: absolute;
    left: 66px; top: 50px;
    width: 344px; height: 562px;
    border-radius: 150px 150px 0 0;
    background: linear-gradient(180deg, #d9c9a4 0%, #cbb89a 18%, #2a2d38 45%, #15171f 100%);
  }
  .initials {
    position: absolute;
    left: 745px; top: 55px;
    width: 212px; height: 197px;
    display: flex; align-items: center; justify-content: center;
    font-family: 'Cinzel', serif;
    font-weight: 600;
    font-size: 96px;
    color: var(--navy);
    letter-spacing: 4px;
  }
  .identity {
    position: absolute;
    left: 628px; top: 272px;
    white-space: nowrap;
  }
  .agent-name {
    font-family: 'Cinzel', serif;
    font-weight: 700;
    font-size: 54px;
    line-height: 1;
    color: var(--navy);
  }
  .agent-title {
    font-family: 'Cinzel', serif;
    font-weight: 600;
    font-size: 30px;
    line-height: 1.2;
    color: var(--ink);
    letter-spacing: 11px;
    margin-top: 6px;
  }
  .agent-license {
    font-family: 'Cinzel', serif;
    font-size: 21px;
    line-height: 1.2;
    color: #333;
    letter-spacing: 8px;
    margin-top: 2px;
  }
  .contacts {
    position: absolute;
    left: 624px; top: 475px;
    list-style: none;
  }
  .contact {
    display: flex; align-items: center;
    height: 44.5px;
    font-family: 'Roboto', sans-serif;
    font-size: 31px;
    color: var(--text-blue);
  }
  .contact svg { width: 40px; height: 36px; margin-right: 12px; flex: none; }
  .band-rule {
    position: absolute; left: 0; top: 608px;
    width: 1200px; height: 5px;
    background: linear-gradient(90deg, var(--gold-dark), var(--gold-light), var(--gold-dark));
  }
  .band {
    position: absolute; left: 0; top: 613px;
    width: 1200px; height: 89px;
    background: linear-gradient(180deg, var(--navy) 0%, var(--navy-deep) 100%);
  }
  .tagline {
    position: absolute; left: 58px; top: 630px;
    width: 1084px; height: 30px;
    background: linear-gradient(90deg, var(--gold-dark), var(--gold-light) 50%, var(--gold-dark));
    display: flex; align-items: center; justify-content: center;
    font-family: 'Cinzel', serif;
    font-weight: 700;
    font-size: 20px;
    letter-spacing: 14px;
    color: var(--navy-deep);
    white-space: nowrap;
  }
</style>
</head>
<body>
<div class="card">
  <div class="headshot" role="img" aria-label="Headshot of Dena Hartwell in a dark blazer, arms crossed"></div>

  <p class="initials">DH</p>

  <div class="identity">
    <h1 class="agent-name">Dena Hartwell</h1>
    <p class="agent-title">REALTOR/BROKER</p>
    <p class="agent-license">CRS/EPro, BRE # 00573846</p>
  </div>

  <ul class="contacts">
    <li class="contact">
      <svg viewBox="0 0 40 36" aria-hidden="true"><path d="M9 4c2-1 4 0 5 2l3 5c1 2 0 3-1 4l-2 2c2 4 5 7 9 9l2-2c1-1 2-2 4-1l5 3c2 1 3 3 2 5l-2 3c-2 2-5 2-8 1C17 31 9 23 5 14 4 11 4 8 6 6z" fill="var(--gold)"/></svg>
      <span>661-548-2907</span>
    </li>
    <li class="contact">
      <svg viewBox="0 0 40 36" aria-hidden="true"><path d="M3 14l17-11 17 11v19H3z" fill="var(--gold)"/><rect x="9" y="8" width="22" height="14" fill="#f4e4b0"/><path d="M3 14l17 12 17-12v19H3z" fill="var(--gold-dark)"/></svg>
      <span>dena@bluevane4homes.example</span>
    </li>
    <li class="contact">
      <svg viewBox="0 0 40 36" aria-hidden="true"><g fill="none" stroke="var(--gold)" stroke-width="2.5"><circle cx="20" cy="18" r="15"/><ellipse cx="20" cy="18" rx="7" ry="15"/><path d="M5 18h30M8 10h24M8 26h24M20 3v30"/></g></svg>
      <span>Bluevanerealestate.example</span>
    </li>
  </ul>

  <div class="band-rule"></div>
  <div class="band"></div>
  <p class="tagline">TURNING REAL ESTATE DREAMS INTO REALITY!</p>
</div>
</body>
</html>
```